TKA Electricial Contracting Services

Hi guys, after a design for my small electrical company, have logo design files to be incorporated into the layout, the basic concept is electrical contracting services for residential, commercial, industrial & data services, image is clean clear and strong,

Card format is to have a nice clean logo on front,with maybe the Residential – commercial – industrial - data, followed with licensed & insured, followed by contact details on backside of the card.

Target Market(s)

Residential, commercial, industrial sectors.

Industry/Entity Type

Electrical

Contact Information for Business Card

TKA logo,
Residential – commercial – industrial - data
REC: 61372
Email: tka@poralink.net.au
Phone: 0458 203 719

Requirements
Must have
• Clean & strong design.
Nice to have
• If possible, I would like the logo colours inverted so the text is orange and the background is black on the front of the card, then the backside of the card be the reverse colour
Should not have
• No Sparks, lightning bolts,

```html
<!DOCTYPE html>
<html lang="en">
<head>
<meta charset="utf-8">
<title>TKA Electrical – Business Card</title>
<link href="https://fonts.googleapis.com/css2?family=Exo+2:wght@500;600;700;800&display=swap" rel="stylesheet">
<style>
  :root {
    --stage: #ebebeb;
    --ink: #111111;
    --orange: #f5862a;
    --orange-light: #f7962f;
    --orange-deep: #f27423;
    --grey: #8a8a8a;
    --grey-dark: #555555;
  }
  * { margin: 0; padding: 0; box-sizing: border-box; }
  html, body {
    width: 1200px; height: 1000px; overflow: hidden;
    background: var(--stage);
    font-family: "Exo 2", sans-serif;
  }
  .canvas { position: relative; width: 1200px; height: 1000px; }

  .card {
    position: absolute;
    width: 560px; height: 320px;
    border-radius: 30px;
    overflow: hidden;
    box-shadow: 0 10px 30px rgba(0,0,0,0.18);
  }

  /* Front */
  .card-front { left: 110px; top: 560px; background: var(--ink); }
  .front-lockup {
    position: absolute; left: 0; right: 0; top: 78px;
    text-align: center; color: var(--orange);
  }
  .front-mark {
    font-weight: 800; font-size: 92px; line-height: 1; letter-spacing: 2px;
  }
  .front-name {
    font-weight: 700; font-size: 22px; margin-top: 6px; letter-spacing: 0.5px;
  }
  .front-sectors {
    color: var(--grey); font-weight: 600; font-size: 15px; margin-top: 4px; letter-spacing: 0.5px;
  }
  .front-licence {
    color: var(--grey-dark); font-weight: 600; font-size: 11px; margin-top: 2px; letter-spacing: 0.5px;
  }

  /* Back */
  .card-back { left: 530px; top: 150px; }
  .back-shapes { position: absolute; inset: 0; }
  .badge {
    position: absolute; left: 34px; top: 0;
    width: 148px; height: 70px;
    background: var(--ink); border-radius: 0 0 10px 10px;
    color: var(--orange); text-align: center; padding-top: 10px;
  }
  .badge-mark { font-weight: 800; font-size: 32px; line-height: 1; letter-spacing: 1px; }
  .badge-name { font-weight: 700; font-size: 10.5px; margin-top: 4px; }
  .holder-name {
    position: absolute; left: 56px; top: 122px;
    font-weight: 800; font-size: 30px; line-height: 40px; color: var(--ink); letter-spacing: 0.5px;
  }
  .contact {
    position: absolute; display: flex; align-items: center; gap: 10px;
    color: var(--orange); font-weight: 600; font-size: 16px; line-height: 26px; letter-spacing: 0.5px;
    white-space: nowrap;
  }
  .contact-email { left: 150px; top: 258px; }
  .contact-phone { left: 400px; top: 146px; }
  .contact-icon { width: 26px; height: 26px; flex: none; }
</style>
</head>
<body>
<main class="canvas">

  <section class="card card-back" aria-label="Business card, contact side">
    <svg class="back-shapes" viewBox="0 0 560 320" width="560" height="320" aria-hidden="true">
      <defs>
        <linearGradient id="backOrange" x1="0" y1="0" x2="0" y2="1">
          <stop offset="0" stop-color="#f7962f"/>
          <stop offset="1" stop-color="#f27423"/>
        </linearGradient>
      </defs>
      <rect width="560" height="320" fill="url(#backOrange)"/>
      <path d="M0 205 H340 C370 205 365 118 400 118 H560 V320 H0 Z" fill="#111111"/>
      <rect x="0" y="169" width="366" height="7" fill="#111111"/>
      <rect x="0" y="185" width="362" height="7" fill="#111111"/>
    </svg>

    <div class="badge">
      <div class="badge-mark">TKA</div>
      <div class="badge-name">Theo Kaine Electrical</div>
    </div>

    <h1 class="holder-name">Theo Kaine</h1>

    <div class="contact contact-phone">
      <svg class="contact-icon" viewBox="0 0 26 26" aria-hidden="true">
        <circle cx="13" cy="13" r="13" fill="#f5862a"/>
        <path d="M9 7.5 l2.5 -0.5 1.4 3.2 -1.6 1.2 c0.8 1.6 1.8 2.6 3.3 3.3 l1.2 -1.6 3.2 1.4 -0.5 2.5 c-5 0.6 -10 -4.4 -9.5 -9.5 Z" fill="#111111"/>
      </svg>
      <span>0458 203 719</span>
    </div>

    <div class="contact contact-email">
      <svg class="contact-icon" viewBox="0 0 26 26" aria-hidden="true">
        <circle cx="13" cy="13" r="13" fill="#f5862a"/>
        <rect x="6.5" y="8.5" width="13" height="9" fill="none" stroke="#111111" stroke-width="1.6"/>
        <path d="M6.5 8.5 L13 13.5 L19.5 8.5" fill="none" stroke="#111111" stroke-width="1.6"/>
      </svg>
      <span>tka@poralink.net.au</span>
    </div>
  </section>

  <section class="card card-front" aria-label="Business card, logo side">
    <div class="front-lockup">
      <div class="front-mark">TKA</div>
      <div class="front-name">Theo Kaine Electrical</div>
      <div class="front-sectors">Residential – Commercial – Industrial</div>
      <div class="front-licence">data REC: 61372</div>
    </div>
  </section>

</main>
</body>
</html>
```